New Company Website

Need a new website for my company Loxley Greenery.
Loxley Greenery offers four business lines: Interior Landscaping, Urbanscaping, Holiday Decorating, and Rental Plants.
Interior Landscaping is the interior installation and maintenance of live plants and flowers in corporate offices. Interiorscape contracts will be for a variety of terms from month to month to 3 years with differing price points in each option.
Urbanscaping refers to landscaping in the urban environment and is restricted in this definition to street side planters and medians, monument plantings and rooftop/balcony gardens.
Holiday Decorating is the Christmas/Hanukkah decorating during the winter season for corporate offices. The model for this business is to lease decorations for a period of 3 years.
Plant rentals is the short term rental of plants and live flowers (orchids, kalanchoe, etc) to event venues. The long term plan is to become the exclusive interior plant vendor for tradeshow organizations in the Tri-State area.

Target Market(s)

Office Managers, Building Managers, Event Coordinators

Industry/Entity Type

Landscaping

Requirements
Must have
• I love my logo. Please incorporate and use colors. Do not change logo.
Nice to have
• These are my competitors:
www.fernhollowdecor.com
www.qorvel.com

```html
<!DOCTYPE html>
<html lang="en">
<head>
<meta charset="utf-8">
<title>Loxley Greenery</title>
<link rel="stylesheet" href="https://fonts.googleapis.com/css2?family=Raleway:wght@300;400;600;700&family=Open+Sans:wght@400;600;700&display=swap">
<style>
:root{
  --blue:#0b8fcf;
  --green:#5fa52f;
  --ink:#333;
  --line:#e3e3e3;
  --footer:#2b2b2b;
  --footer-deep:#1b1b1b;
  --footer-text:#b5b5b5;
}
*{margin:0;padding:0;box-sizing:border-box}
html,body{width:1200px;height:2229px;overflow:hidden;background:#fff}
body{position:relative;font-family:"Open Sans",Arial,sans-serif;color:var(--ink)}
.abs{position:absolute}

/* header */
.brand{left:40px;top:22px;display:flex;align-items:center;gap:12px}
.brand-dot{width:46px;height:46px;border-radius:50%;background:var(--blue)}
.brand-name{font-family:"Raleway",sans-serif;font-weight:700;font-size:34px;color:var(--green);letter-spacing:-.5px}
.search{left:970px;top:18px;width:188px;height:31px;border:1px solid var(--line);font-size:14px;color:#999;padding:6px 12px}
.search svg{position:absolute;right:10px;top:8px}
.nav-rule{left:0;top:103px;width:1200px;height:1px;background:var(--line)}
.nav-active{left:36px;top:101px;width:131px;height:3px;background:var(--blue)}
.nav{left:0;top:127px;width:1200px}
.nav-item{position:absolute;font-family:"Raleway",sans-serif}
.nav-item b{display:block;font-size:14px;font-weight:700;color:#333}
.nav-item span{display:block;font-size:12px;color:#999;margin-top:5px;letter-spacing:.3px}
.nav-item.is-current b{color:var(--blue)}
.nav-item svg{position:absolute;top:4px}
.nav-bottom{left:0;top:192px;width:1200px;height:1px;background:var(--line)}

/* hero */
.hero{left:0;top:193px;width:1200px;height:466px;background:linear-gradient(180deg,#5a4330 0%,#8b6b4a 35%,#c9b79a 55%,#6e5236 80%,#3a2a1c 100%)}
.dots{left:533px;top:628px;display:flex;gap:10px}
.dots i{width:14px;height:14px;border-radius:50%;border:2px solid #fff}
.dots i.on{background:#fff}

/* service cards */
.card{position:absolute;width:562px;height:246px;display:flex}
.card-photo{width:274px;height:100%}
.card-body{flex:1;background:var(--blue);padding:10px 24px;color:#fff}
.card-title{font-family:"Raleway",sans-serif;font-weight:400;font-size:23px}
.card-text{font-family:"Raleway",sans-serif;font-weight:700;font-size:19px;line-height:26px;margin-top:14px}
.card-btn{display:inline-block;margin-top:14px;width:138px;height:36px;border:1px solid rgba(255,255,255,.45);background:rgba(255,255,255,.12);font-family:"Raleway",sans-serif;font-size:14px;text-align:center;line-height:34px;letter-spacing:.5px}

/* about */
.about-title{left:35px;top:1282px;font-family:"Raleway",sans-serif;font-weight:300;font-size:52px;color:#333;letter-spacing:-1px}
.about-sub{left:35px;top:1354px;font-family:"Raleway",sans-serif;font-size:17px;color:#555}
.about-photo{left:35px;top:1427px;width:477px;height:320px;background:radial-gradient(ellipse at 45% 45%,#8fbf3c 0%,#5f8f22 55%,#3c6416 100%)}
.about-copy{left:608px;top:1426px;width:500px}
.about-copy h3{font-family:"Raleway",sans-serif;font-weight:400;font-size:20px;color:#333}
.about-copy p{font-family:Arial,sans-serif;font-size:15.5px;line-height:23.5px;color:#555;margin-top:18px}
.about-copy .fine{font-size:12px;color:#888;margin-top:20px}
.about-copy a{display:block;font-family:"Raleway",sans-serif;font-size:16px;color:var(--blue);text-decoration:none;margin-top:22px}

/* footer */
.footer{left:0;top:1774px;width:1200px;height:455px;background:var(--footer);border-top:4px solid var(--blue)}
.f-col{position:absolute;top:80px;width:260px;color:var(--footer-text)}
.f-col h4{font-family:"Open Sans",sans-serif;font-weight:700;font-size:13px;color:#fff;letter-spacing:.3px;padding-bottom:10px;border-bottom:1px solid #3c3c3c}
.f-col p{font-size:13px;line-height:20px;margin-top:44px}
.f-col .copy{margin-top:40px}
.tweet{margin-top:38px;width:260px;height:60px;background:#242424;position:relative;padding:10px 14px;font-size:13px}
.tweet small{position:absolute;right:40px;top:6px;font-size:11px;color:#ddd;font-weight:600}
.tweet a{display:block;margin-top:18px;color:#5bb8e8}
.socials{display:flex;gap:17px;margin-top:32px}
.socials i{width:38px;height:39px;background:#363636}
.flickr{margin:38px 0 0 21px;display:grid;grid-template-columns:repeat(3,72px);grid-auto-rows:64px;gap:1px;width:218px}
.flickr i:nth-child(3n+1){background:linear-gradient(135deg,#3d5a5a,#7b6a4e)}
.flickr i:nth-child(3n+2){background:linear-gradient(135deg,#2f4f5f,#5e8a6e)}
.flickr i:nth-child(3n){background:linear-gradient(135deg,#4e6b4a,#9fb9b5)}
.contact dl{margin-top:42px;font-size:13px;line-height:21px}
.contact dt{display:inline;font-weight:700;color:#ccc}
.contact dd{display:inline}
.contact div{margin-bottom:10px}
.bottom-bar{left:23px;top:2177px;width:1147px;height:52px;background:var(--footer-deep);padding:16px 34px;font-size:12px;color:#aaa}
.bottom-bar span{margin:0 8px;color:#555}
</style>
</head>
<body>

<header>
  <div class="abs brand"><div class="brand-dot"></div><div class="brand-name">Loxley Greenery</div></div>
  <div class="abs search">Search...
    <svg width="14" height="14" viewBox="0 0 14 14"><circle cx="6" cy="6" r="4.5" fill="none" stroke="#aaa" stroke-width="1.5"/><line x1="9.3" y1="9.3" x2="13" y2="13" stroke="#aaa" stroke-width="1.5"/></svg>
  </div>
  <div class="abs nav-rule"></div>
  <div class="abs nav-active"></div>
  <nav class="abs nav">
    <div class="nav-item is-current" style="left:42px"><b>HOME</b><span>ALL START HERE</span><svg style="left:110px" width="10" height="6"><path d="M1 1l4 4 4-4" fill="none" stroke="#999"/></svg></div>
    <div class="nav-item" style="left:213px"><b>PAGES</b><span>TEMPLATE FEATURES</span><svg style="left:137px" width="10" height="6"><path d="M1 1l4 4 4-4" fill="none" stroke="#999"/></svg></div>
    <div class="nav-item" style="left:411px"><b>ABOUT</b><span>TIME TO MEET MARLOW</span><svg style="left:150px" width="10" height="6"><path d="M1 1l4 4 4-4" fill="none" stroke="#999"/></svg></div>
    <div class="nav-item" style="left:622px"><b>BLOG</b><span>WHAT WE THINK</span><svg style="left:92px" width="10" height="6"><path d="M1 1l4 4 4-4" fill="none" stroke="#999"/></svg></div>
    <div class="nav-item" style="left:776px"><b>PORTFOLIO</b><span>THINGS WE HAVE DONE</span><svg style="left:145px" width="10" height="6"><path d="M1 1l4 4 4-4" fill="none" stroke="#999"/></svg></div>
  </nav>
  <div class="abs nav-bottom"></div>
</header>

<section class="abs hero" role="img" aria-label="Bright living room with cream sofas, large potted palms and open terrace doors"></section>
<div class="abs dots"><i class="on"></i><i></i><i></i><i></i><i></i></div>

<section>
  <article class="card" style="left:35px;top:701px">
    <div class="card-photo" role="img" aria-label="Office atrium with tall indoor trees and river stones" style="background:linear-gradient(160deg,#6b6f6a,#4a5a3a 50%,#7a6a55)"></div>
    <div class="card-body"><div class="card-title">Interior Landscaping</div><div class="card-text">Live plants and flowers installed and cared for in your corporate offices</div><div class="card-btn">VIEW MORE</div></div>
  </article>
  <article class="card" style="left:597px;top:701px">
    <div class="card-photo" role="img" aria-label="Formal garden with hedges and a grass path" style="background:linear-gradient(180deg,#4f7a3a,#6f9a3f 60%,#9cc25a)"></div>
    <div class="card-body"><div class="card-title">Urbanscaping</div><div class="card-text">Street planters, medians and rooftop gardens</div><div class="card-btn">VIEW MORE</div></div>
  </article>
  <article class="card" style="left:35px;top:989px;height:253px">
    <div class="card-photo" role="img" aria-label="Living room with fireplace and decorated holiday tree" style="background:linear-gradient(160deg,#8a7a66,#5e4a38 55%,#3f2c1f)"></div>
    <div class="card-body"><div class="card-title">Holiday Decorating</div><div class="card-text">Christmas and Hanukkah décor for offices, leased on simple three-year terms</div><div class="card-btn">VIEW MORE</div></div>
  </article>
  <article class="card" style="left:597px;top:989px;height:249px">
    <div class="card-photo" role="img" aria-label="Lush display of tropical potted plants" style="background:linear-gradient(180deg,#3f6a7a,#3c5a2e 55%,#2b3a1e)"></div>
    <div class="card-body"><div class="card-title">Rental Plants</div><div class="card-text">Short-term plants and orchids for event venues</div><div class="card-btn">VIEW MORE</div></div>
  </article>
</section>

<section>
  <h2 class="abs about-title">Find Everything about Us.</h2>
  <p class="abs about-sub">Living greenery for offices, buildings and events, planted and cared for by our team.</p>
  <div class="abs about-photo" role="img" aria-label="World map shaped from green grass"></div>
  <div class="abs about-copy">
    <h3>What We Do ?</h3>
    <p>We bring live plants to the places people work and gather. Office managers get installed, maintained plants and flowers. Building managers get street planters, medians, monument beds and rooftop gardens. Event coordinators rent orchids and kalanchoe for a day or a week, and each winter we dress offices for the holidays.</p>
    <p class="fine">Contracts from month to month up to three years</p>
    <a href="#">Discover more about our plant care contracts &rsaquo;</a>
  </div>
</section>

<footer class="abs footer">
  <div class="f-col" style="left:35px">
    <h4>DISCLAIMER</h4>
    <p>Important: plant care terms, prices and availability vary by contract length and location. Rental plants are subject to venue access and season.</p>
    <p class="copy">© 2012. All Rights Reserved.<br>Powered by</p>
  </div>
  <div class="f-col" style="left:323px">
    <h4>STAY CONNECTED</h4>
    <div class="tweet"><small>Latest tweet</small><a>@loxleyleaf</a></div>
    <div class="socials"><i></i><i></i><i></i><i></i></div>
  </div>
  <div class="f-col" style="left:611px">
    <h4>FLICKR PHOTOSTREAM</h4>
    <div class="flickr" role="img" aria-label="Grid of nine small garden photographs"><i></i><i></i><i></i><i></i><i></i><i></i><i></i><i></i><i></i></div>
  </div>
  <div class="f-col contact" style="left:897px">
    <h4>CONTACT INFORMATION</h4>
    <dl>
      <div><dt>Address:</dt> <dd>No.28 - 63739 street lorem ipsum City, Country</dd></div>
      <div><dt>Phone:</dt> <dd>+ 1 (234) 567 8901</dd></div>
      <div><dt>Fax:</dt> <dd>+ 1 (234) 567 8901</dd></div>
      <div><dt>Email:</dt> <dd>hello@loxleygreenery.com</dd></div>
    </dl>
  </div>
</footer>
<div class="abs bottom-bar">Home<span>|</span>About<span>|</span>Contact<span>|</span>Blog<span>|</span>Portfolio</div>

</body>
</html>
```